11 month inspection POST CARD for Brightkeel Home Inspections

a post card size flyer to new home owners from Brightkeel Home Inspections.
Use text from this. front and back if needed.
Brightkeel Home Inspections
555-318-7046
www.BrightkeelHomeInspections.example
Your Trusted Home Inspection Experts
"Protect Your Investment!"
11-Month Home Inspection Reminder
Don't Let Your Builder's Warranty Expire
Congratulations on your new home! As trusted home inspection experts, Brightkeel Home Inspections wants to ensure your peace of mind. Did you know that most builders offer a 1-year warranty on their construction? Now is the perfect time to schedule your 11-month inspection before your warranty expires.
Our comprehensive inspection will evaluate the key areas of your home to identify any potential issues covered under your builder's warranty. Our certified inspectors will thoroughly examine the structure, plumbing, electrical systems, HVAC, roofing, and more. Identifying these issues early can save you thousands of dollars in future repairs.
[Bullet Points]
- Early detection of hidden defects
- Maximize your builder's warranty coverage
- Protect your investment
- Ensure a safe and comfortable living environment
- Expert advice and recommendations
[Call to Action]
Schedule your 11-Month Inspection today!
Brightkeel Home Inspections
Your Partner in Home Ownership
[Back of the Postcard]
Why Choose Brightkeel Home Inspections?
[Bullet Points]
- Trusted industry professionals with over 20 years of experience
- Certified and licensed inspectors
- Thorough and comprehensive inspections
- Detailed inspection reports with photos
- Excellent customer service and support
- Competitive pricing and value
Brightkeel Home Inspections
873 SW 29th Ave, Ocala, FL USA
Visit: www.brightkeelhomeinspections.example
Remember, time is of the essence! Schedule your 11-month inspection today to ensure your builder addresses any issues covered under warranty. We look forward to helping you protect your investment and enjoy your new home worry-free!
Sincerely,
Brightkeel Home Inspections
555-318-7046
Target Market(s)
New Home Owners
Industry/Entity Type
Inspections
Requirements
Must have
- Our logo, phone number, website
Nice to have
- eye catching

```html
<!DOCTYPE html>
<html lang="en">
<head>
<meta charset="utf-8">
<title>Brightkeel Home Inspections – 11-Month Inspection Postcard</title>
<link href="https://fonts.googleapis.com/css2?family=Poppins:wght@400;500;600;700;800&display=swap" rel="stylesheet">
<style>
  :root{
    --blue:#1c58a8;
    --blue-dark:#173f7d;
    --red:#e21b2b;
    --ink:#4a4a4a;
    --paper:#ffffff;
    --backdrop:#e4e4e4;
    --rule:#c9c9c9;
  }
  *{box-sizing:border-box;margin:0;padding:0}
  html,body{width:1200px;height:900px;overflow:hidden}
  body{background:var(--backdrop);font-family:'Poppins',sans-serif;color:var(--ink);position:relative}

  .postcard{position:absolute;left:285px;width:630px;height:420px;background:var(--paper);overflow:hidden;box-shadow:0 10px 24px rgba(0,0,0,.18)}
  .postcard--front{top:20px}
  .postcard--back{top:460px}

  .house-photo{position:absolute;inset:0;background:linear-gradient(160deg,#f6f7f8 0%,#e3e6e8 45%,#d9dcd6 75%,#e9ebe8 100%);opacity:.9}
  .house-photo::after{content:"";position:absolute;inset:0;background:rgba(255,255,255,.55)}

  .brand-mark{position:absolute;left:22px;top:22px;display:flex;align-items:center;gap:7px;width:150px}
  .brand-mark__dot{width:30px;height:30px;border-radius:50%;background:var(--blue);flex:none}
  .brand-mark__name{font-size:11px;font-weight:700;line-height:1.15;color:var(--blue-dark);text-transform:uppercase}

  /* front */
  .front-header{position:absolute;right:34px;top:24px;text-align:right;text-transform:uppercase;line-height:1.15}
  .front-header__name{color:var(--blue);font-size:14px;font-weight:700}
  .front-header__tagline{color:var(--red);font-size:14px;font-weight:800}

  .headline-band{position:absolute;left:96px;right:40px;top:72px;height:48px;background:var(--blue);color:#fff;font-size:29px;font-weight:800;text-transform:uppercase;display:flex;align-items:center;justify-content:center;letter-spacing:.5px}
  .headline-sub{position:absolute;left:96px;right:40px;top:122px;text-align:center;color:var(--red);font-size:19px;font-weight:800;text-transform:uppercase}

  .warranty-column{position:absolute;left:26px;top:166px;width:310px}
  .bar{color:#fff;font-weight:700;text-transform:uppercase;text-align:center;line-height:1.2}
  .bar--blue{background:var(--blue);font-size:11px;padding:5px 8px}
  .bar--red{background:var(--red);font-size:11.5px;padding:5px 8px}
  .warranty-copy{font-size:8.2px;line-height:1.45;margin-top:6px;color:var(--ink)}
  .warranty-copy + .warranty-copy{margin-top:5px}
  .warranty-copy strong{color:var(--red);font-weight:700}
  .warranty-copy .accent-blue{color:var(--blue)}

  .phone{display:flex;align-items:center;gap:6px;color:var(--blue);font-weight:800;letter-spacing:.5px}
  .front-phone{position:absolute;left:30px;top:338px;font-size:31px}
  .phone svg{flex:none}

  .benefits-column{position:absolute;left:350px;top:160px;width:252px}
  .bullet-list{list-style:none}
  .bullet-list li{position:relative;padding-left:11px}
  .bullet-list li::before{content:"";position:absolute;left:0;width:5px;height:5px;border-radius:50%;background:var(--blue)}
  .benefits-list{margin-top:8px;font-size:10px;line-height:1.3}
  .benefits-list li{margin-bottom:5px}
  .benefits-list li::before{top:5px}

  .partner-line{position:absolute;right:34px;top:320px;text-align:right;text-transform:uppercase;line-height:1.15}
  .partner-line__name{color:var(--blue);font-size:12.5px;font-weight:700}
  .partner-line__tagline{color:var(--red);font-size:12.5px;font-weight:800}

  .footer-band{position:absolute;left:0;right:0;bottom:0;height:30px;background:var(--red);color:#fff;font-size:12px;font-weight:600;display:flex;align-items:center;justify-content:flex-end;padding-right:40px}

  /* back */
  .why-title{position:absolute;left:26px;top:68px;text-transform:uppercase;font-weight:800;line-height:1.05}
  .why-title__lead{color:var(--red);font-size:22px}
  .why-title__name{color:var(--blue);font-size:20px}
  .why-rule{position:absolute;left:26px;top:120px;width:370px;height:3px;background:var(--red)}

  .reasons-list{position:absolute;left:34px;top:132px;width:330px;font-size:12.5px;line-height:1.25;font-weight:500}
  .reasons-list li{margin-bottom:6px}
  .reasons-list li::before{top:6px}

  .back-address{position:absolute;left:34px;top:306px;display:flex;gap:5px;font-size:10px;line-height:1.3}
  .back-address svg{margin-top:2px}
  .back-phone{position:absolute;left:34px;top:338px;font-size:28px}

  .stamp-box{position:absolute;right:26px;top:26px;width:72px;height:72px;border:1.5px solid #9a9a9a}
  .mailing-lines{position:absolute;left:392px;right:26px;top:124px}
  .mailing-lines span{display:block;height:1px;background:var(--rule);margin-bottom:22px}

  .closing-note{position:absolute;left:392px;top:222px;width:212px;font-size:10.5px;line-height:1.35}
  .closing-note strong{color:var(--red);font-weight:800;font-size:13px}
  .closing-note .accent-blue{color:var(--blue);font-weight:700}
  .sign-off{position:absolute;left:400px;top:340px;font-size:11px;line-height:1.3}
</style>
</head>
<body>

<section class="postcard postcard--front" aria-label="Postcard front">
  <div class="house-photo" role="img" aria-label="Faded photograph of a new two-storey family home with landscaped front yard"></div>

  <div class="brand-mark">
    <span class="brand-mark__dot"></span>
    <span class="brand-mark__name">Brightkeel Home Inspections</span>
  </div>

  <div class="front-header">
    <p class="front-header__name">Brightkeel Home Inspections</p>
    <p class="front-header__tagline">Your Trusted Home Inspection Experts</p>
  </div>

  <h1 class="headline-band">Protect Your Investment!</h1>
  <p class="headline-sub">11-Month Home Inspection Reminder</p>

  <div class="warranty-column">
    <p class="bar bar--blue">Don't Let Your Builder's Warranty Expire</p>
    <p class="warranty-copy"><strong>Congratulations</strong> on your new home! As trusted home inspection experts, Brightkeel Home Inspections wants to ensure your peace of mind. Did you know that most builders offer a 1-year warranty on their construction? Now is the perfect time to schedule your 11-month inspection before your warranty expires.</p>
    <p class="warranty-copy"><strong class="accent-blue">Our comprehensive</strong> inspection will evaluate the key areas of your home to identify any potential issues covered under your builder's warranty. Our certified inspectors will thoroughly examine the structure, plumbing, electrical systems, HVAC, roofing, and more. Identifying these issues early can save you thousands of dollars in future repairs.</p>
  </div>

  <p class="phone front-phone">
    <svg width="26" height="26" viewBox="0 0 24 24" aria-hidden="true"><circle cx="12" cy="12" r="12" fill="#1c58a8"/><path d="M8.2 6.5l2 .3.8 2.6-1.3 1.1a7 7 0 003.8 3.8l1.1-1.3 2.6.8.3 2c-.2.8-1 1.3-1.8 1.2A10 10 0 017 8.3c-.1-.8.4-1.6 1.2-1.8z" fill="#fff"/></svg>
    555-318-7046
  </p>

  <div class="benefits-column">
    <p class="bar bar--red">Schedule your 11-Month<br>Inspection Today!</p>
    <ul class="bullet-list benefits-list">
      <li>Early detection of hidden defects</li>
      <li>Maximize your builder's warranty coverage</li>
      <li>Protect your investment</li>
      <li>Ensure a safe and comfortable living environment</li>
      <li>Expert advice and recommendations</li>
    </ul>
  </div>

  <div class="partner-line">
    <p class="partner-line__name">Brightkeel Home Inspections</p>
    <p class="partner-line__tagline">Your Partner in Home Ownership</p>
  </div>

  <p class="footer-band">www.brightkeelhomeinspections.example</p>
</section>

<section class="postcard postcard--back" aria-label="Postcard back">
  <div class="house-photo" role="img" aria-label="Faded photograph of a new two-storey family home"></div>

  <div class="brand-mark">
    <span class="brand-mark__dot"></span>
    <span class="brand-mark__name">Brightkeel Home Inspections</span>
  </div>

  <h2 class="why-title">
    <span class="why-title__lead">Why Choose</span><br>
    <span class="why-title__name">Brightkeel Home Inspections?</span>
  </h2>
  <div class="why-rule"></div>

  <ul class="bullet-list reasons-list">
    <li>Trusted industry professionals with over 20 years of experience</li>
    <li>Certified and licensed inspectors</li>
    <li>Thorough and comprehensive inspections</li>
    <li>Detailed inspection reports with photos</li>
    <li>Excellent customer service and support</li>
    <li>Competitive pricing and value</li>
  </ul>

  <div class="back-address">
    <svg width="9" height="12" viewBox="0 0 10 14" aria-hidden="true"><path d="M5 0a5 5 0 015 5c0 3.5-5 9-5 9S0 8.5 0 5a5 5 0 015-5z" fill="#e21b2b"/><circle cx="5" cy="5" r="1.8" fill="#fff"/></svg>
    <p>Brightkeel Home Inspections<br>873 SW 29th Ave, Ocala, FL USA</p>
  </div>

  <p class="phone back-phone">
    <svg width="22" height="22" viewBox="0 0 24 24" aria-hidden="true"><circle cx="12" cy="12" r="12" fill="#1c58a8"/><path d="M8.2 6.5l2 .3.8 2.6-1.3 1.1a7 7 0 003.8 3.8l1.1-1.3 2.6.8.3 2c-.2.8-1 1.3-1.8 1.2A10 10 0 017 8.3c-.1-.8.4-1.6 1.2-1.8z" fill="#fff"/></svg>
    555-318-7046
  </p>

  <div class="stamp-box" aria-label="Stamp area"></div>
  <div class="mailing-lines" aria-hidden="true"><span></span><span></span><span></span><span></span></div>

  <p class="closing-note"><strong>Remember</strong>, time is of the essence! Schedule your 11-month inspection today to ensure your builder addresses any issues covered under warranty. We look forward to helping you protect your investment and enjoy your new home <span class="accent-blue">worry-free!</span></p>

  <p class="sign-off">Sincerely,<br>Brightkeel Home Inspections</p>

  <p class="footer-band">www.brightkeelhomeinspections.example</p>
</section>

</body>
</html>
```